Melvin Otrasko Consulting Corporation
Independent Insurance and Reinsurance Consultants
Melvin Otrasko Consulting Corporation - Consulting
Creative Brief
Professional
Melvin Otrasko, (omitted)
Principal Consultant
3816C Verlune Court Carlsbad, CA 92011
motrasko@motraskoadvise.com
www.motraskoadvise.com

```html
<!DOCTYPE html>
<html lang="en">
<head>
<meta charset="utf-8">
<title>Melvin Otrasko Consulting Corporation – Stationery</title>
<link rel="stylesheet" href="https://fonts.googleapis.com/css2?family=Open+Sans:wght@400;600&display=swap">
<style>
  :root{
    --bg:#e9e9e9;
    --paper:#ffffff;
    --navy:#10306a;
    --blue:#2a6fc4;
    --sky:#8ec3ee;
    --ink:#5a5a5a;
    --rule:#9a9a9a;
    --pale:#d6e6f8;
    --shadow:0 1px 3px rgba(0,0,0,.18);
  }
  *{box-sizing:border-box;margin:0;padding:0}
  html,body{width:1200px;height:552px;overflow:hidden;background:var(--bg)}
  body{position:relative;font-family:"Open Sans",Arial,sans-serif;color:var(--ink)}
  .sheet{position:absolute;background:var(--paper);box-shadow:var(--shadow);overflow:hidden}
  .swoosh{position:absolute;left:0;bottom:0;width:100%;display:block}

  .wordmark{position:absolute;font-family:"Open Sans",Arial,sans-serif;font-weight:600;color:var(--blue);white-space:nowrap;line-height:1}

  .contact{position:absolute;list-style:none;font-size:5px;line-height:7.4px;color:var(--ink)}
  .contact li{display:flex;align-items:center;gap:3px;white-space:nowrap}
  .contact li::before{content:"";width:4px;height:4px;border-radius:50%;background:var(--blue);flex:none}

  /* fax */
  .fax{left:14px;top:17px;width:363px;height:506px}
  .fax .wordmark{left:15px;top:26px;font-size:11px}
  .fax-title{position:absolute;right:18px;top:78px;font-size:11px;font-weight:600;color:#333;letter-spacing:.05em}
  .fax-table{position:absolute;left:15px;top:94px;width:333px;border-collapse:collapse;font-size:6px;color:#444}
  .fax-table td{border:1px solid var(--rule);height:14.3px;padding:0 4px}
  .fax-table .lbl{width:42px}
  .fax-options{position:absolute;left:15px;top:181px;display:flex;gap:20px;font-size:5.5px;color:#444;list-style:none}
  .fax-options li{display:flex;align-items:center;gap:3px;white-space:nowrap}
  .fax-options li::before{content:"";width:6px;height:6px;border:1px solid #666;background:#fff}

  /* letterhead */
  .letter{left:403px;top:17px;width:355px;height:506px}
  .letter .wordmark{left:15px;top:26px;font-size:11px}

  /* cards */
  .card-front{left:780px;top:24px;width:144px;height:82px}
  .card-front .wordmark{left:8px;top:10px;font-size:5.6px}
  .card-name{position:absolute;left:8px;top:34px;font-size:5px;font-weight:600;color:#333}
  .card-role{position:absolute;left:8px;top:41px;font-size:3.8px;color:var(--ink)}
  .card-front .contact{left:8px;top:48px;font-size:3.6px;line-height:5px}
  .card-front .contact li::before{width:3px;height:3px}
  .card-back{left:938px;top:24px;width:156px;height:82px;border-radius:4px;
    background:radial-gradient(ellipse at 50% 45%, #2d5fae 0%, var(--navy) 70%)}
  .card-back .web{position:absolute;right:10px;bottom:10px;font-size:4px;color:#b9d2ef;letter-spacing:.05em}

  /* envelope front */
  .env-front{left:780px;top:127px;width:396px;height:202px}
  .env-front .wordmark{left:14px;top:22px;font-size:11px}
  .env-front .contact{left:14px;top:134px}

  /* envelope back */
  .env-back{left:780px;top:360px;width:396px;height:163px}
  .env-flap{position:absolute;left:0;top:0;width:100%;height:100%}
  .env-back .wordmark{left:0;right:0;top:66px;text-align:center;font-size:11px;color:var(--pale)}
</style>
</head>
<body>

<svg width="0" height="0" style="position:absolute" aria-hidden="true">
  <defs>
    <linearGradient id="waveFill" x1="0" y1="0" x2="1" y2="0">
      <stop offset="0" stop-color="#5d9fe0"/>
      <stop offset=".45" stop-color="#1f58a8"/>
      <stop offset="1" stop-color="#10306a"/>
    </linearGradient>
    <radialGradient id="flapFill" cx=".5" cy=".35" r=".7">
      <stop offset="0" stop-color="#3a72c2"/>
      <stop offset=".6" stop-color="#1a4288"/>
      <stop offset="1" stop-color="#10306a"/>
    </radialGradient>
  </defs>
</svg>

<!-- Fax cover -->
<section class="sheet fax">
  <div class="wordmark">Melvin Otrasko Consulting Corporation</div>
  <ul class="contact" style="left:282px;top:14px">
    <li>Melvin Otrasko</li>
    <li>3816C Verlune Court</li>
    <li>Harlow Bay, CA 90000</li>
    <li>motrasko@motraskoadvise.com</li>
    <li>www.motraskoadvise.com</li>
  </ul>
  <div class="fax-title">FAX</div>
  <table class="fax-table">
    <tr><td class="lbl">To:</td><td></td><td class="lbl">From:</td><td></td></tr>
    <tr><td class="lbl">Fax:</td><td></td><td class="lbl">Pages:</td><td></td></tr>
    <tr><td class="lbl">Phone:</td><td></td><td class="lbl">Date:</td><td></td></tr>
    <tr><td class="lbl">Re:</td><td></td><td class="lbl">CC:</td><td></td></tr>
  </table>
  <ul class="fax-options">
    <li>Urgent</li><li>For Review</li><li>Please Comment</li><li>Please Reply</li><li>Please Recycle</li>
  </ul>
  <svg class="swoosh" viewBox="0 0 360 60" preserveAspectRatio="none" height="60" aria-hidden="true">
    <path d="M0 60 L0 56 Q190 44 360 8 L360 60 Z" fill="url(#waveFill)"/>
    <path d="M0 50 Q190 38 360 2" fill="none" stroke="#8ec3ee" stroke-width="1"/>
  </svg>
</section>

<!-- Letterhead -->
<section class="sheet letter">
  <div class="wordmark">Melvin Otrasko Consulting Corporation</div>
  <ul class="contact" style="left:278px;top:14px">
    <li>Melvin Otrasko</li>
    <li>3816C Verlune Court</li>
    <li>Harlow Bay, CA 90000</li>
    <li>motrasko@motraskoadvise.com</li>
    <li>www.motraskoadvise.com</li>
  </ul>
  <svg class="swoosh" viewBox="0 0 360 60" preserveAspectRatio="none" height="60" aria-hidden="true">
    <path d="M0 60 L0 56 Q190 44 360 8 L360 60 Z" fill="url(#waveFill)"/>
    <path d="M0 50 Q190 38 360 2" fill="none" stroke="#8ec3ee" stroke-width="1"/>
  </svg>
</section>

<!-- Business card front -->
<section class="sheet card-front">
  <div class="wordmark">Melvin Otrasko Consulting Corporation</div>
  <div class="card-name">Melvin Otrasko</div>
  <div class="card-role">Principal Consultant</div>
  <ul class="contact">
    <li>3816C Verlune Court, Harlow Bay, CA 90000</li>
    <li>motrasko@motraskoadvise.com</li>
    <li>www.motraskoadvise.com</li>
  </ul>
  <svg class="swoosh" viewBox="0 0 144 20" preserveAspectRatio="none" height="18" aria-hidden="true">
    <path d="M0 20 L0 18 Q80 14 144 2 L144 20 Z" fill="url(#waveFill)"/>
    <path d="M0 15 Q80 11 144 0" fill="none" stroke="#8ec3ee" stroke-width=".6"/>
  </svg>
</section>

<!-- Business card back -->
<section class="sheet card-back">
  <div class="web">www.motraskoadvise.com</div>
</section>

<!-- Envelope front -->
<section class="sheet env-front">
  <div class="wordmark">Melvin Otrasko Consulting Corporation</div>
  <ul class="contact">
    <li>Melvin Otrasko</li>
    <li>3816C Verlune Court</li>
    <li>Harlow Bay, CA 90000</li>
    <li>motrasko@motraskoadvise.com</li>
    <li>www.motraskoadvise.com</li>
  </ul>
  <svg class="swoosh" viewBox="0 0 396 40" preserveAspectRatio="none" height="40" aria-hidden="true">
    <path d="M0 40 L0 37 Q210 30 396 4 L396 40 Z" fill="url(#waveFill)"/>
    <path d="M0 31 Q210 24 396 0" fill="none" stroke="#8ec3ee" stroke-width="1"/>
  </svg>
</section>

<!-- Envelope back -->
<section class="sheet env-back">
  <svg class="env-flap" viewBox="0 0 396 163" preserveAspectRatio="none" aria-hidden="true">
    <path d="M0 0 H396 V112 L198 150 L0 112 Z" fill="url(#flapFill)"/>
    <path d="M0 112 L198 150 L396 112" fill="none" stroke="#8ec3ee" stroke-width="1"/>
  </svg>
  <div class="wordmark">Melvin Otrasko Consulting Corporation</div>
</section>

</body>
</html>
```